Web site for cutting edge executive coaching and consulting firm | ||
Bravonte | ||
Consulting | ||
Services that increase Performance: - Coaching: Executives, Groups / Teams - Problem Solving - Organizational Change. Focus on: - Holistic approach - Verdessan spirit (colors) - Psychological driven models - Relationship building - sustained outcomes |
I like colors, yet, colors shall not hinder clear reading of text. I like a clear & simple structure of Website. I like to use symbols and/or forms. |
Cutting-Edge Unique/Creative Clean/Simple Professional Exciting Industrial Colorful Elegant Progressive Service Oriented Traditional |
blue | ||
Arial Verdana |

```html
<!DOCTYPE html>
<html lang="en">
<head>
<meta charset="utf-8">
<title>Bravonte – Executive Coaching and Consulting</title>
<link rel="stylesheet" href="https://fonts.googleapis.com/css2?family=Arimo:wght@400;700&display=swap">
<style>
  :root {
    --backdrop: #0b0b10;
    --glow-red: #c8321c;
    --glow-blue: #1e5fd6;
    --glow-green: #1fbf4a;
    --panel: #ffffff;
    --ink: #2d2d2d;
    --ink-soft: #555a60;
    --brand-blue: #1f3f96;
    --swoosh-green: #48b24a;
    --swoosh-blue: #2a78c8;
    --band-grey: #e7e8ea;
    --band-grey-dark: #cfd1d4;
    --footer: #f4f4f5;
    --video: #d9dadc;
    --icon-green: #6fae3f;
    --icon-red: #c8462e;
    --icon-tan: #d9935a;
  }
  * { box-sizing: border-box; margin: 0; padding: 0; }
  html, body { width: 1200px; height: 790px; overflow: hidden; }
  body {
    font-family: "Arimo", Arial, sans-serif;
    color: var(--ink);
    background:
      radial-gradient(ellipse 420px 520px at 40px 420px, var(--glow-red), transparent 70%),
      radial-gradient(ellipse 520px 260px at 600px 0px, var(--glow-blue), transparent 72%),
      radial-gradient(ellipse 460px 560px at 1160px 330px, var(--glow-green), transparent 70%),
      var(--backdrop);
    position: relative;
  }
  .site {
    position: absolute;
    left: 180px; top: 96px;
    width: 840px; height: 600px;
    background: var(--panel);
    border-radius: 14px;
    overflow: hidden;
    box-shadow: 0 10px 40px rgba(0,0,0,.55);
  }
  .site-header { position: relative; height: 150px; }
  .swoosh { position: absolute; left: 0; top: 0; width: 840px; height: 150px; }
  .brand {
    position: absolute; left: 26px; top: 20px;
    display: flex; align-items: center; gap: 10px;
  }
  .brand-mark { width: 14px; height: 14px; background: var(--icon-red); border-radius: 50%; }
  .brand-name { font-size: 40px; font-weight: 700; color: var(--brand-blue); letter-spacing: .5px; }
  .brand-sub {
    position: absolute; left: 52px; top: 66px;
    font-size: 8px; letter-spacing: 3px; color: var(--brand-blue);
  }
  .tagline {
    position: absolute; right: 26px; top: 40px;
    font-size: 11.5px; letter-spacing: 1.4px; color: var(--ink-soft);
  }
  .main-nav {
    position: absolute; left: 170px; top: 140px;
    display: flex; font-size: 13px;
  }
  .main-nav a {
    color: var(--ink); text-decoration: none;
    padding: 0 8px; border-left: 1px solid #b8b8b8;
  }
  .main-nav a:first-child { border-left: none; }
  .welcome { position: absolute; left: 24px; top: 188px; width: 500px; }
  .welcome h1 { font-size: 19px; font-weight: 400; margin-bottom: 12px; }
  .welcome p { font-size: 11.5px; line-height: 1.32; color: var(--ink-soft); }
  .video {
    position: absolute; left: 552px; top: 187px;
    width: 257px; height: 168px;
    background: linear-gradient(#e6e7e9, var(--video));
    border: 1px solid #c4c5c8; border-radius: 8px;
    display: flex; flex-direction: column; align-items: center; justify-content: center; gap: 6px;
    font-size: 12px; color: var(--ink-soft);
  }
  .play {
    width: 44px; height: 30px; border-radius: 5px; background: #a8aaae;
    display: flex; align-items: center; justify-content: center;
  }
  .services {
    position: absolute; left: 0; top: 372px;
    width: 840px; height: 161px;
    background: linear-gradient(var(--band-grey), var(--band-grey-dark));
  }
  .arrow { position: absolute; top: 70px; width: 10px; height: 14px; }
  .arrow.prev { left: 12px; }
  .arrow.next { right: 12px; }
  .service { position: absolute; top: 14px; width: 230px; }
  .service:nth-of-type(1) { left: 52px; }
  .service:nth-of-type(2) { left: 300px; }
  .service:nth-of-type(3) { left: 546px; }
  .service-head { display: flex; align-items: center; gap: 10px; margin-bottom: 10px; }
  .service-icon { width: 34px; height: 34px; border-radius: 6px; }
  .service-icon.team { background: var(--icon-green); }
  .service-icon.relation { background: var(--icon-red); border-radius: 50%; }
  .service-icon.solve { background: var(--icon-tan); }
  .service h2 { font-size: 15px; font-weight: 400; }
  .service p { font-size: 9.5px; line-height: 1.3; color: var(--ink-soft); }
  .site-footer {
    position: absolute; left: 0; top: 533px; width: 840px; height: 67px;
    background: var(--footer); border-top: 1px solid #dcdcdc;
    font-size: 9.5px; color: var(--ink-soft); text-align: center;
  }
  .copyright { margin-top: 13px; }
  .contact { margin-top: 6px; display: flex; justify-content: center; gap: 16px; }
  .contact span { display: inline-flex; align-items: center; gap: 5px; }
  .social { position: absolute; left: 18px; top: 26px; display: flex; gap: 6px; }
  .social span { width: 20px; height: 20px; border-radius: 3px; background: #8c8f94; }
</style>
</head>
<body>
  <div class="site">
    <header class="site-header">
      <svg class="swoosh" viewBox="0 0 840 150" aria-hidden="true">
        <defs>
          <linearGradient id="swooshFill" x1="0" x2="1">
            <stop offset="0" stop-color="var(--swoosh-blue)"/>
            <stop offset=".45" stop-color="var(--swoosh-green)"/>
            <stop offset="1" stop-color="var(--swoosh-green)"/>
          </linearGradient>
        </defs>
        <path d="M0 110 C220 70 520 60 840 95 L840 130 C560 92 260 100 0 140 Z" fill="url(#swooshFill)" opacity=".85"/>
        <path d="M0 140 C260 100 560 92 840 130 L840 150 L0 150 Z" fill="#f7f7f7"/>
      </svg>
      <div class="brand">
        <span class="brand-mark"></span>
        <span class="brand-name">Bravonte</span>
      </div>
      <div class="brand-sub">EXECUTIVE INSIGHT</div>
      <div class="tagline">CUTTING EDGE EXECUTIVE COACHING AND CONSULTING</div>
      <nav class="main-nav">
        <a href="#">Home</a><a href="#">About Us</a><a href="#">Services</a><a href="#">News</a><a href="#">Contact Us</a><a href="#">Members</a>
      </nav>
    </header>

    <section class="welcome">
      <h1>Welcome to Bravonte website</h1>
      <p>Lorem ipsum dolor sit amet, consectetuer adipiscing elit, sed diam nonummy nibh euismod tincidunt ut laoreet dolore magna aliquam erat volutpat. Ut wisi enim ad minim veniam, quis nostrud exerci tation ullamcorper suscipit lobortis nisl ut aliquip ex ea commodo consequat. Duis autem vel eum iriure dolor in hendrerit in vulputate velit esse molestie consequat, vel illum dolore eu feugiat nulla facilisis at vero eros et accumsan et iusto odio dignissim qui blandit praesent luptatum zzril delenit augue duis dolore te feugait nulla facilisi. Ut wisi enim ad minim veniam, quis nostrud exerci tation ullamcorper suscipit.</p>
    </section>

    <div class="video">
      Watch video
      <span class="play"><svg width="14" height="16" viewBox="0 0 14 16" aria-hidden="true"><path d="M0 0 L14 8 L0 16 Z" fill="#fff"/></svg></span>
    </div>

    <section class="services">
      <svg class="arrow prev" viewBox="0 0 10 14" aria-hidden="true"><path d="M10 0 L0 7 L10 14 Z" fill="#9a9ca0"/></svg>
      <article class="service">
        <div class="service-head"><span class="service-icon team" role="img" aria-label="Puzzle piece icon"></span><h2>Part of the Team</h2></div>
        <p>Lorem ipsum dolor sit amet, consectetuer adipiscing elit, sed diam nonummy nibh euismod tincidunt ut laoreet dolore magna aliquam erat volutpat. Ut wisi enim ad minim veniam, quis nostrud exerci tation ullamcorper suscipit lobortis nisl ut aliquip.</p>
      </article>
      <article class="service">
        <div class="service-head"><span class="service-icon relation" role="img" aria-label="Linked network icon"></span><h2>Relationship Building</h2></div>
        <p>Lorem ipsum dolor sit amet, consectetuer adipiscing elit, sed diam nonummy nibh euismod tincidunt ut laoreet dolore magna aliquam erat volutpat. Ut wisi enim ad minim veniam, quis nostrud exerci tation ullamcorper suscipit lobortis nisl ut aliquip.</p>
      </article>
      <article class="service">
        <div class="service-head"><span class="service-icon solve" role="img" aria-label="Pointing hand icon"></span><h2>Problem Solving</h2></div>
        <p>Lorem ipsum dolor sit amet, consectetuer adipiscing elit, sed diam nonummy nibh euismod tincidunt ut laoreet dolore magna aliquam erat volutpat. Ut wisi enim ad minim veniam, quis nostrud exerci tation ullamcorper suscipit lobortis nisl ut aliquip.</p>
      </article>
      <svg class="arrow next" viewBox="0 0 10 14" aria-hidden="true"><path d="M0 0 L10 7 L0 14 Z" fill="#9a9ca0"/></svg>
    </section>

    <footer class="site-footer">
      <div class="social" aria-label="Social links"><span></span><span></span><span></span></div>
      <p class="copyright">© 2011 Bravonte. All Rights Reserved.</p>
      <p class="contact">
        <span><svg width="10" height="10" viewBox="0 0 10 10" aria-hidden="true"><path d="M2 0 L4 3 L3 4 Q4 6 6 7 L7 6 L10 8 L8 10 Q2 9 0 2 Z" fill="#777"/></svg>555-014-2290</span>
        <span><svg width="11" height="8" viewBox="0 0 11 8" aria-hidden="true"><rect x=".5" y=".5" width="10" height="7" fill="none" stroke="#777"/><path d="M.5 .5 L5.5 4.5 L10.5 .5" fill="none" stroke="#777"/></svg>info@bravonte.com</span>
      </p>
    </footer>
  </div>
</body>
</html>
```